Funeral Services Site

We need a website for a Funeral Services company. The old website is: www.rouwcentrumkorvelaer.be We need the same structure and text.

Target Market(s)

Customers.

Coding

Coded - Design and coding required

Number of Pages Required

4 page

Font styles to use
Serif
Sans Serif
Script

```html
<!DOCTYPE html>
<html lang="en">
<head>
<meta charset="utf-8">
<title>Funeral Home Korvelaer Bvba</title>
<link rel="stylesheet" href="https://fonts.googleapis.com/css2?family=Poppins:wght@400;500&family=Montserrat:wght@400;500;600&family=Raleway:wght@300;400&display=swap">
<style>
:root{
  --red:#e84c3d;
  --ink:#1f2a3a;
  --text:#2b2b2b;
  --dark:#2f2f2f;
  --dark-2:#3a3a3a;
  --light:#f1f1f1;
  --white:#ffffff;
  --line:#d9d9d9;
}
*{margin:0;padding:0;box-sizing:border-box}
html,body{width:1200px;height:3232px;overflow:hidden}
body{position:relative;background:var(--white);font-family:"Montserrat",sans-serif;color:var(--text)}
.abs{position:absolute}

/* header */
.site-header{position:absolute;left:0;top:0;width:1200px;height:97px;border-top:3px solid var(--red);border-bottom:1px solid var(--line);background:var(--white);z-index:3}
.brand-badge{position:absolute;left:143px;top:-47px;width:207px;height:207px;border-radius:50%;background:var(--white);box-shadow:0 4px 10px rgba(0,0,0,.25);z-index:5;display:flex;align-items:flex-end;justify-content:center;padding-bottom:48px;text-align:center;font-family:"Poppins",sans-serif;font-size:15px;line-height:18px;color:var(--text)}
.phone-tab{position:absolute;left:838px;top:0;width:244px;height:33px;background:var(--red);border-radius:0 0 14px 14px;clip-path:polygon(0 0,100% 0,94% 100%,6% 100%);color:var(--white);font-family:"Poppins",sans-serif;font-size:16px;display:flex;align-items:center;justify-content:center;gap:10px;white-space:nowrap}
.main-nav{position:absolute;top:56px;left:0;width:1200px;font-family:"Montserrat",sans-serif;font-size:15px;font-weight:500;color:var(--text)}
.main-nav span{position:absolute;white-space:nowrap}
.main-nav .active{color:var(--red)}

/* hero */
.hero-photo{position:absolute;left:0;top:97px;width:1200px;height:438px;background:linear-gradient(100deg,#2a2a2c 0%,#3a3a3d 18%,#8a6a55 30%,#c88a5e 48%,#b86a3e 62%,#7a5a3a 78%,#c9c9b8 92%,#eeeeea 100%)}
.slider-arrow{position:absolute;top:304px;width:30px;height:24px;background:#3a3a3a;display:flex;align-items:center;justify-content:center}
.hero-card{position:absolute;left:234px;top:498px;width:730px;height:188px;background:var(--white);border-top:3px solid var(--red);box-shadow:0 6px 14px rgba(0,0,0,.12);text-align:center;font-family:"Poppins",sans-serif;color:var(--ink)}
.hero-card h1{font-weight:400;font-size:28px;line-height:38px;margin-top:17px}
.call-pill{display:inline-flex;align-items:center;justify-content:center;gap:14px;height:46px;padding:0 22px;border:2px solid var(--red);border-radius:24px;font-family:"Poppins",sans-serif;font-size:17px;color:var(--ink);background:var(--white);white-space:nowrap}
.call-pill b{font-weight:500}

/* section titles */
.section-title{position:absolute;left:0;width:1200px;text-align:center;font-family:"Poppins",sans-serif;font-weight:400;color:var(--text)}
.title-rule{position:absolute;height:2px;background:#555}

.about-sub{position:absolute;left:0;top:828px;width:1200px;text-align:center;font-size:17.5px;font-weight:500}
.about-text{position:absolute;left:150px;top:861px;width:900px;text-align:center;font-size:13px;line-height:23px}
.btn-red{position:absolute;background:var(--red);color:var(--white);border-radius:16px;display:flex;align-items:center;justify-content:center;font-family:"Montserrat",sans-serif;white-space:nowrap}

/* organization */
.ceremony-photo{position:absolute;left:143px;top:1151px;width:388px;height:375px;background:linear-gradient(180deg,#5a3216 0%,#6e3e1c 40%,#d9d6c8 62%,#3f5a2e 78%,#2b3a66 100%);box-shadow:0 6px 12px rgba(0,0,0,.2)}
.ceremony-copy{position:absolute;left:553px;top:1189px;width:510px;font-size:12.5px;line-height:25px}
.ceremony-copy p{margin-bottom:12px}
.ceremony-copy h3{font-family:"Montserrat",sans-serif;font-weight:500;font-size:17.5px;margin:4px 0 8px}
.arrange-list{list-style:none;font-family:"Poppins",sans-serif;font-size:13px;line-height:23px}
.arrange-list li{position:relative;padding-left:26px;margin-bottom:12px}
.arrange-list svg{position:absolute;left:0;top:5px}

/* services band */
.band-left{position:absolute;left:0;top:1614px;width:614px;height:479px;background:var(--dark)}
.band-right{position:absolute;left:614px;top:1614px;width:586px;height:479px;background:var(--dark-2)}
.band-col{position:absolute;text-align:center;color:var(--white)}
.band-col h2{font-family:"Raleway",sans-serif;font-weight:300;font-size:32px;line-height:38px;color:var(--red)}
.band-col .rule{width:36px;height:2px;background:var(--white);margin:14px auto 16px}
.band-col p{font-size:13px;line-height:23px}

/* quick contact */
.contact-area{position:absolute;left:0;top:2093px;width:1200px;height:539px;background:var(--light)}
.intro-text{position:absolute;left:160px;top:2234px;width:880px;text-align:center;font-size:13px;line-height:23px}
.field{position:absolute;background:var(--white);border:1px solid var(--line);border-radius:2px;font-size:11px;font-weight:600;color:#333;padding:8px 15px}

/* cta */
.cta-question{position:absolute;left:0;top:2710px;width:1200px;text-align:center;font-family:"Montserrat",sans-serif;font-size:19px;line-height:36px;color:#333;text-transform:uppercase}
.cta-pill{position:absolute;left:416px;top:2795px;width:353px;height:45px;padding:0 16px;gap:12px}

/* footer */
.site-footer{position:absolute;left:0;top:2918px;width:1200px;height:266px;background:var(--dark-2);color:var(--white)}
.footer-heading{position:absolute;font-family:"Poppins",sans-serif;font-size:15px}
.footer-rule{position:absolute;width:36px;height:2px;background:var(--white)}
.footer-links{position:absolute;left:143px;top:85px;list-style:none;font-size:12px;line-height:27px}
.footer-item{position:absolute;left:404px;font-size:11.5px;line-height:18px;white-space:nowrap}
.footer-icon{position:absolute;left:373px}
.footer-brand{position:absolute;left:780px;top:112px;width:290px;display:flex;align-items:center;gap:12px;font-family:"Poppins",sans-serif;font-size:24px;line-height:28px;font-weight:500;color:var(--white)}
.footer-brand i{display:block;width:40px;height:40px;border-radius:50%;border:2px solid var(--white);flex:none}
.copyright{position:absolute;left:0;top:3184px;width:1200px;height:48px;background:var(--red);color:var(--white);font-size:12px;display:flex;align-items:center;justify-content:center;white-space:nowrap}
</style>
</head>
<body>

<header class="site-header">
  <div class="phone-tab">
    <svg width="20" height="20" viewBox="0 0 24 24" fill="none" stroke="#fff" stroke-width="1.8"><circle cx="12" cy="12" r="10.5"/><path d="M8 6.5l2 2.5-1.2 1.5c.8 1.7 2 2.9 3.7 3.7l1.5-1.2 2.5 2-1 1.8c-3.8-.3-7.2-3.7-7.5-7.5z" fill="#fff" stroke="none"/></svg>
    1-555-014-2870
  </div>
  <nav class="main-nav">
    <span class="active" style="left:500px">Home</span>
    <span style="left:583px">About Us</span>
    <span style="left:686px">Condole Online</span>
    <span style="left:835px">Order Flowers</span>
    <span style="left:973px">Contact Us</span>
  </nav>
</header>
<div class="brand-badge">Funeral Home<br>Korvelaer Bvba</div>

<section>
  <div class="hero-photo" role="img" aria-label="Mourner in a dark suit laying a red rose on a wooden coffin decorated with white flowers"></div>
  <div class="slider-arrow" style="left:3px"><svg width="8" height="12" viewBox="0 0 8 12"><path d="M6 1L2 6l4 5" stroke="#fff" stroke-width="2" fill="none"/></svg></div>
  <div class="slider-arrow" style="left:1166px"><svg width="8" height="12" viewBox="0 0 8 12"><path d="M2 1l4 5-4 5" stroke="#fff" stroke-width="2" fill="none"/></svg></div>
  <div class="hero-card">
    <h1>Funeral Home Korvelaer Bvba:<br>A Personal Service In Farewell Guidance</h1>
    <div class="call-pill" style="margin-top:14px">Contact Us Today
      <svg width="24" height="24" viewBox="0 0 24 24" fill="none" stroke="#1f2a3a" stroke-width="1.6"><circle cx="12" cy="12" r="10.5"/><path d="M8 6.5l2 2.5-1.2 1.5c.8 1.7 2 2.9 3.7 3.7l1.5-1.2 2.5 2-1 1.8c-3.8-.3-7.2-3.7-7.5-7.5z" fill="#1f2a3a" stroke="none"/></svg>
      <b>1-555-014-2870</b></div>
  </div>
</section>

<section>
  <h2 class="section-title" style="top:763px;font-size:32px">About Us</h2>
  <div class="title-rule" style="top:809px;left:527px;width:146px;height:1.5px"></div>
  <p class="about-sub">Mourning center Korvelaer, a complete service in mourning and farewell guidance</p>
  <p class="about-text">Saying goodbye to a loved one is one of the toughest things in a lifetime. Funeral home Korvelaer in Oudenhoven takes care of all the practical and administrative matters involved. So you can say goodbye in peace.<br>Our people have a rich experience in farewell guidance and stand for 24 hours at 24 hours for you. Our fully renovated funeral home is open to you and your acquaintances, so that you can greet your loved one at any time of the day.</p>
  <div class="btn-red" style="left:540px;top:966px;width:113px;height:30px;font-size:15px;font-weight:600">Read More</div>
</section>

<section>
  <h2 class="section-title" style="top:1077px;font-size:34px">Organization Funeral And Worship</h2>
  <div class="title-rule" style="top:1127px;left:537px;width:124px;height:1.5px"></div>
  <div class="ceremony-photo" role="img" aria-label="Brass cross behind an arrangement of white orchids and calla lilies"></div>
  <div class="ceremony-copy">
    <p>The organization of the funeral ceremony is a moment of reflection, where the personality of the deceased can be beautifully highlighted. Our team will assist you in this and select the most beautiful texts, songs and photos with you in order to arrive at an appropriate and worthy goodbye.</p>
    <p>The funeral can take place in your parish church or &nbsp;our auditorium if you wish, which can accommodate a maximum of 100 guests.</p>
    <h3>We can arrange the following for you:</h3>
    <ul class="arrange-list">
      <li><svg width="14" height="14" viewBox="0 0 14 14" fill="none" stroke="#e84c3d" stroke-width="1.4"><circle cx="7" cy="7" r="5.8"/><path d="M4 7l2.2 2.2L13 2.5"/></svg>Vigil The Night Before The Funeral</li>
      <li><svg width="14" height="14" viewBox="0 0 14 14" fill="none" stroke="#e84c3d" stroke-width="1.4"><circle cx="7" cy="7" r="5.8"/><path d="M4 7l2.2 2.2L13 2.5"/></svg>Prayer Service With Priest (if Possible)</li>
      <li><svg width="14" height="14" viewBox="0 0 14 14" fill="none" stroke="#e84c3d" stroke-width="1.4"><circle cx="7" cy="7" r="5.8"/><path d="M4 7l2.2 2.2L13 2.5"/></svg>Eucharistic Celebration With Priest<br>(on Tuesday And Friday In The Parishes Of Oudenhoven)</li>
    </ul>
  </div>
</section>

<section>
  <div class="band-left"></div>
  <div class="band-right"></div>
  <div class="band-col" style="left:130px;top:1740px;width:380px">
    <h2>Condole Online via<br>the website</h2>
    <div class="rule"></div>
    <p>Do you want to leave nice words to the family of a deceased person?<br>Funeral home Korvelaer gives you the opportunity to convey your message quickly and discreetly</p>
  </div>
  <div class="btn-red" style="left:256px;top:1944px;width:113px;height:30px;font-size:16px">Get Started</div>

  <svg class="abs" style="left:518px;top:1786px" width="164" height="164" viewBox="0 0 164 164" fill="none" aria-hidden="true">
    <circle cx="82" cy="82" r="81" stroke="#4a4a4a"/>
    <circle cx="82" cy="82" r="65" stroke="#555"/>
    <circle cx="82" cy="82" r="49" stroke="#fff" stroke-width="2"/>
  </svg>

  <div class="band-col" style="left:688px;top:1737px;width:380px">
    <h2>Reserve Flower<br>Arrangement</h2>
    <div class="rule"></div>
    <p>In the funeral home there is always an engaging selection of floral arrangements and wreaths .<br>If you want to order fresh flowers, consult the catalog in the store or complete the order form</p>
  </div>
  <div class="btn-red" style="left:819px;top:1950px;width:113px;height:30px;font-size:16px">Get Started</div>
</section>

<section class="contact-area"></section>
<h2 class="section-title" style="top:2175px;font-size:34px">Quick Contact</h2>
<div class="title-rule" style="top:2224px;left:552px;width:96px;height:1.5px"></div>
<p class="intro-text">Lorem ipsum dolor sit amet, consectetuer adipiscing elit, sed diam nonummy nibh euismod tincidunt ut laoreet dolore magna aliquam erat volutpat. Ut wisi enim ad minim veniam.</p>
<div class="field" style="left:301px;top:2292px;width:290px;height:38px;padding-top:5px">First Name</div>
<div class="field" style="left:608px;top:2292px;width:290px;height:38px;padding-top:18px">Last Name</div>
<div class="field" style="left:301px;top:2344px;width:290px;height:38px;padding-top:5px">Email</div>
<div class="field" style="left:608px;top:2344px;width:290px;height:38px;padding-top:18px">Phone</div>
<div class="field" style="left:301px;top:2402px;width:597px;height:84px">Message</div>
<div class="btn-red" style="left:543px;top:2508px;width:106px;height:30px;font-size:12px;font-weight:600">SUBMIT</div>

<section>
  <p class="cta-question">Do you have any questions or would you like to call in our funeral home?<br>Contact us. We are here for you.</p>
  <div class="call-pill cta-pill">Contact Us Today
    <svg width="24" height="24" viewBox="0 0 24 24" fill="none" stroke="#1f2a3a" stroke-width="1.6"><circle cx="12" cy="12" r="10.5"/><path d="M8 6.5l2 2.5-1.2 1.5c.8 1.7 2 2.9 3.7 3.7l1.5-1.2 2.5 2-1 1.8c-3.8-.3-7.2-3.7-7.5-7.5z" fill="#1f2a3a" stroke="none"/></svg>
    <b>1-555-014-2870</b></div>
</section>

<footer class="site-footer">
  <div class="footer-heading" style="left:143px;top:36px">Quick Links</div>
  <div class="footer-rule" style="left:143px;top:67px"></div>
  <ul class="footer-links">
    <li>Home</li><li>About Us</li><li>Condole Online</li><li>Order Flowers</li><li>Contact Us</li>
  </ul>

  <div class="footer-heading" style="left:374px;top:38px">Contact Details</div>
  <div class="footer-rule" style="left:374px;top:67px"></div>
  <svg class="footer-icon" style="top:92px" width="14" height="18" viewBox="0 0 14 18"><path d="M7 0a6 6 0 00-6 6c0 4.5 6 12 6 12s6-7.5 6-12a6 6 0 00-6-6zm0 8.5A2.5 2.5 0 117 3.5a2.5 2.5 0 010 5z" fill="#fff"/></svg>
  <div class="footer-item" style="top:92px">Funeral Home Korvelaer Bvba:<br>Veldstraat 18, 3700 Oudenhoven</div>
  <svg class="footer-icon" style="top:156px" width="18" height="18" viewBox="0 0 24 24" fill="none" stroke="#fff" stroke-width="1.6"><circle cx="12" cy="12" r="10.5"/><path d="M8 6.5l2 2.5-1.2 1.5c.8 1.7 2 2.9 3.7 3.7l1.5-1.2 2.5 2-1 1.8c-3.8-.3-7.2-3.7-7.5-7.5z" fill="#fff" stroke="none"/></svg>
  <div class="footer-item" style="top:156px">24/24, 7 out of 7 &nbsp;- 012 00 41 77</div>
  <svg class="footer-icon" style="top:200px" width="18" height="13" viewBox="0 0 18 13" fill="none" stroke="#fff" stroke-width="1.3"><rect x=".7" y=".7" width="16.6" height="11.6"/><path d="M.7.7L9 7.5 17.3.7"/></svg>
  <div class="footer-item" style="top:197px">contact@rouwcentrumkorvelaer.be</div>

  <div class="footer-brand"><span>Funeral home<br>Korvelaer bvba</span><i></i></div>
</footer>
<div class="copyright">Copyright © 2019 &nbsp;2018 Northgate Media &nbsp;- Sitemap &nbsp;- Privacy Policy</div>

</body>
</html>
```